Criação de Kit com 6 Layouts de Post para Redes Sociais (Facebook, Instagram e etc) + Capa de Facebook para Educação & Cursos
A empresa queria:
" Atuação no mercado corporativo, com cursos, palestras e programas de desenvolvimento das pessoas no ambiente de trabalho. "

```html
<!DOCTYPE html>
<html lang="pt-BR">
<head>
<meta charset="UTF-8">
<title>Curso de Oratória – Turma confirmada</title>
<link rel="stylesheet" href="https://fonts.googleapis.com/css2?family=Poppins:wght@400;500;600;700&display=swap">
<style>
  :root {
    --navy-deep: #0a1a4a;
    --navy: #10245f;
    --blue-pill: #1848d0;
    --blue-pill-light: #2f66ee;
    --warm-dark: #4a2016;
    --warm: #b4482a;
    --warm-mid: #6a3038;
    --yellow: #f6b325;
    --white: #ffffff;
  }
  * { margin: 0; padding: 0; box-sizing: border-box; }
  html, body { width: 1200px; height: 1200px; overflow: hidden; }
  body { font-family: "Poppins", sans-serif; background: var(--navy-deep); }

  .post {
    position: relative;
    width: 1200px;
    height: 1200px;
    overflow: hidden;
  }

  .post__photo {
    position: absolute;
    inset: 0;
    background: linear-gradient(170deg, var(--warm-dark) 0%, var(--warm) 28%, var(--warm-mid) 46%, var(--navy) 62%, var(--navy-deep) 100%);
  }

  .accent-bar {
    position: absolute;
    background: var(--yellow);
    border-radius: 40px;
  }
  .accent-bar--top { left: 43px; top: -80px; width: 72px; height: 267px; }
  .accent-bar--bottom { left: 1037px; top: 1078px; width: 82px; height: 200px; }

  .brand {
    position: absolute;
    left: 770px;
    top: 66px;
    color: var(--white);
    font-weight: 700;
    font-size: 80px;
    line-height: 1;
    letter-spacing: -1px;
  }

  .pill {
    position: absolute;
    left: 50%;
    transform: translateX(-50%);
    display: flex;
    align-items: center;
    justify-content: center;
    color: var(--white);
    background: linear-gradient(180deg, var(--blue-pill-light) 0%, var(--blue-pill) 100%);
    border-radius: 40px;
    white-space: nowrap;
  }
  .pill--course { top: 624px; width: 677px; height: 76px; font-size: 52px; font-weight: 600; }
  .pill--date   { top: 826px; width: 560px; height: 68px; font-size: 45px; font-weight: 500; }
  .pill--venue  { top: 912px; width: 677px; height: 74px; font-size: 46px; font-weight: 500; }

  .headline {
    position: absolute;
    left: 0;
    width: 100%;
    top: 728px;
    text-align: center;
    color: var(--white);
    font-size: 65px;
    font-weight: 600;
    line-height: 1.2;
  }

  .quote {
    position: absolute;
    left: 0;
    width: 100%;
    top: 1028px;
    text-align: center;
    color: var(--white);
    font-size: 30px;
    font-weight: 500;
    line-height: 41px;
  }
  .quote__author {
    display: block;
    font-size: 24px;
    font-weight: 400;
    line-height: 32px;
    margin-top: 0;
  }
</style>
</head>
<body>
  <main class="post">
    <div class="post__photo" role="img" aria-label="Fotografia de um palestrante diante de uma plateia num auditório com luz quente"></div>

    <span class="accent-bar accent-bar--top"></span>
    <span class="accent-bar accent-bar--bottom"></span>

    <div class="brand">Vir</div>

    <div class="pill pill--course">CURSO DE ORATÓRIA</div>
    <h1 class="headline">Turma confirmada</h1>
    <div class="pill pill--date">01 e 02 de abril de 2024</div>
    <div class="pill pill--venue">Espaço Jardim Claro</div>

    <p class="quote">
      “O homem que lê é cheio. O homem que escreve é exato.<br>
      O homem que fala é pronto”
      <span class="quote__author">Henrique Vasconcelos</span>
    </p>
  </main>
</body>
</html>
```